Wix based template. A business card website

Only WixOnly chosen template , no coding!Already bought and activated domain1-Only a ready solution from you as a designer: to load and run2-No mock-ups as a final product of this project: we rquire only a ready solution which can be directly applied and ran on our domain3-no blog, no shop, no email address options required4-only intorduction and information content through 3 web-pages5- home page: a scroll-down template6-content types: pictures, texts, 1 video7- no junior designers8- only a dedicated designer which is available daily and replies in communication quickly enough (within some hours)

Target Market(s)

Corporate business coaching in the area of IT and technology. Emotional intelligence for IT and diversity professionals

Coding

Coded - Design and coding required

Number of Pages Required

3 page

Colors
33b8a4
abd036

Requirements
Must have
• look up at the webpage i have activated with the purchased domain already: brindlecove.com
• So I have a simple but very welcoming business card telling about me, my services and my clients
• The theme please try to allign with my logo ( look inthe uploads)
• as well I would like to use my professional pictures but not too many of them because the website is for the clients as a target .
Nice to have
• example website:
• tilbergvast.nl

```html
<!DOCTYPE html>
<html lang="en">
<head>
<meta charset="utf-8">
<title>Brindle Cove — Services</title>
<link href="https://fonts.googleapis.com/css2?family=Montserrat:wght@400;500;600&family=Roboto:wght@400&display=swap" rel="stylesheet">
<style>
:root{
  --teal-dark:#0c4a45;
  --teal:#33b8a4;
  --lime:#abd036;
  --green:#5ad12f;
  --green-light:#8ef06a;
  --ink:#333333;
  --footer:#333333;
  --white:#ffffff;
}
*{margin:0;padding:0;box-sizing:border-box}
html,body{width:1200px;height:2953px;overflow:hidden;background:var(--white)}
body{position:relative;font-family:Arial,Helvetica,sans-serif;color:var(--ink)}
.top-strip{position:absolute;left:0;top:0;width:1200px;height:4px;background:linear-gradient(90deg,var(--teal),var(--lime))}
.site-header{position:absolute;left:0;top:4px;width:1200px;height:106px;background:var(--white)}
.brand{position:absolute;left:120px;top:32px;display:flex;align-items:center;gap:10px;font-family:Montserrat,sans-serif;font-weight:500;font-size:25px;letter-spacing:5px;color:var(--teal-dark)}
.brand-dot{width:14px;height:14px;border-radius:50%;background:var(--green)}
.main-nav{position:absolute;top:50px;left:488px;display:flex;gap:38px;font-family:Montserrat,sans-serif;font-weight:500;font-size:13.5px;color:#222;letter-spacing:.3px}
.main-nav .active{color:#2a8a6a}
.hero{position:absolute;left:0;top:110px;width:1200px;height:660px;
  background:
    radial-gradient(ellipse 220px 300px at 560px 330px,rgba(120,100,90,.55),transparent 70%),
    radial-gradient(ellipse 200px 260px at 120px 250px,rgba(60,110,40,.6),transparent 70%),
    linear-gradient(100deg,#1d3a1c 0%,#2b3a2f 35%,#1c4438 65%,#0f3b35 100%)}
.hero-wave{position:absolute;left:0;top:700px;width:1200px;height:80px}
.intro-title{position:absolute;left:0;top:822px;width:1200px;text-align:center;font-family:Montserrat,sans-serif;font-weight:500;font-size:31px;color:var(--teal-dark);letter-spacing:.5px}
.intro-sub{position:absolute;left:0;top:876px;width:1200px;text-align:center;font-family:Montserrat,sans-serif;font-size:23px;color:var(--green)}
.service{position:absolute;left:0;width:1200px;height:470px}
.service-text{position:absolute;width:470px}
.service-text h2{font-family:Montserrat,sans-serif;font-weight:500;font-size:23.5px;color:var(--teal-dark);letter-spacing:.5px;margin-bottom:26px}
.service-text p{font-size:12.6px;line-height:27.5px;text-align:justify;margin-bottom:27px;color:#333}
.btn{display:inline-flex;align-items:center;gap:10px;margin-top:3px;width:148px;height:55px;padding-left:13px;border:2px solid #2e7a5a;background:linear-gradient(90deg,#2f8f6a,var(--green-light));color:var(--white);font-family:Montserrat,sans-serif;font-weight:600;font-size:14.5px;box-shadow:0 2px 4px rgba(0,0,0,.25)}
.btn svg{width:18px;height:18px}
.frame{position:absolute;width:394px;height:400px;border-top:4px solid;border-left:4px solid;border-image:linear-gradient(90deg,var(--teal),var(--lime)) 1;border-right:0;border-bottom:0}
.frame::after{content:"";position:absolute;right:-4px;top:-4px;width:4px;height:14px;background:var(--lime)}
.photo{position:absolute;width:396px;height:403px}
.photo-coach{background:
  radial-gradient(ellipse 110px 200px at 190px 240px,rgba(90,80,85,.6),transparent 70%),
  linear-gradient(100deg,#2c3f25,#1e3a2e 50%,#17423a)}
.photo-notes{background:
  radial-gradient(ellipse at 35% 35%,#d9a874,transparent 55%),
  linear-gradient(160deg,#8b6a3c,#b58a52 50%,#3b4a3a 85%,#2a2a24)}
.photo-laptop{background:
  radial-gradient(ellipse at 60% 70%,#3a3a3e,transparent 55%),
  linear-gradient(135deg,#c9b7a2,#a48c74 40%,#5d5452 75%,#2a2a2a)}
.footer{position:absolute;left:0;top:2500px;width:1200px;height:453px}
.footer-wave{position:absolute;left:0;top:0;width:1200px;height:100px}
.footer-body{position:absolute;left:0;top:80px;width:1200px;height:373px;background:var(--footer)}
.footer-brand{position:absolute;left:0;top:170px;width:1200px;display:flex;justify-content:center;align-items:center;gap:18px;font-family:Montserrat,sans-serif;font-weight:500;font-size:48px;letter-spacing:12px;color:var(--teal)}
.footer-brand .brand-dot{width:24px;height:24px}
.footer-nav{position:absolute;left:0;top:290px;width:1200px;text-align:center;font-family:Montserrat,sans-serif;font-size:16px;color:var(--white)}
.footer-nav span{margin:0 11px}
.copyright{position:absolute;left:0;top:335px;width:1200px;text-align:center;font-family:Roboto,sans-serif;font-size:15px;color:#e6e6e6}
.social{position:absolute;left:533px;top:380px;display:flex;gap:6px}
.social i{display:block;width:29px;height:29px;border:2px solid var(--white);border-radius:50%}
</style>
</head>
<body>
<div class="top-strip"></div>
<header class="site-header">
  <div class="brand"><span>BRINDLE COVE</span><span class="brand-dot"></span></div>
  <nav class="main-nav">
    <span>HOME</span><span>ABOUT US</span><span class="active">SERVICES</span><span>NEWS</span><span>TESTIMONIALS</span><span>CONTACT US</span>
  </nav>
</header>

<div class="hero" role="img" aria-label="Smiling businesswoman in a dark suit standing by a glass door, greenery behind her"></div>
<svg class="hero-wave" viewBox="0 0 1200 80" preserveAspectRatio="none">
  <path d="M0 70 C300 0 600 40 1200 38 L1200 80 L0 80 Z" fill="#fff"/>
  <path d="M0 62 C250 10 550 30 800 40 C1000 48 1120 40 1200 40" stroke="#5ad12f" stroke-width="10" fill="none"/>
  <path d="M0 68 C300 20 650 48 900 58 C1050 62 1150 55 1200 45" stroke="#0c4a45" stroke-width="5" fill="none"/>
</svg>

<h1 class="intro-title">SED UT PERSPICIATIS UNDE OMNIS ISTE NATUS</h1>
<p class="intro-sub">voluptatem accusantium doloremque laudantium</p>

<section class="service" style="top:982px">
  <div class="service-text" style="left:130px;top:48px">
    <h2>ONE ON ONE COACHING SESSIONS</h2>
    <p>Sed ut perspiciatis unde omnis iste natus error sit voluptatem accusantium dolor emque laudantium, totam rem aperiam, eaque ipsa quae ab illo inventore veritatis et quasi architecto beatae vitae dicta sunt explicabo. Nemo enim ipsam voluptatem quia voluptas sit aspernatur aut odit aut fugit, sed quia consequuntur magni dolores eos qui ratione voluptatem sequi nesciunt.</p>
    <p>Neque porro quisquam est, qui dolorem ipsum quia dolor sit amet, consectetur, adipisci velit, sed quia non numquam eius modi tempora</p>
    <span class="btn">READ MORE <svg viewBox="0 0 20 20"><circle cx="10" cy="10" r="9" fill="#fff"/><path d="M5 10h8M10 6l4 4-4 4" stroke="#3a9a6a" stroke-width="2.4" fill="none"/></svg></span>
  </div>
  <div class="frame" style="left:661px;top:0"></div>
  <div class="photo photo-coach" style="left:675px;top:15px" role="img" aria-label="Portrait of the coach in a dark suit beside a glass door"></div>
</section>

<section class="service" style="top:1497px">
  <div class="frame" style="left:130px;top:0"></div>
  <div class="photo photo-notes" style="left:143px;top:15px" role="img" aria-label="Close-up of a hand writing with a pen on a notepad"></div>
  <div class="service-text" style="left:601px;top:42px">
    <h2>INTRODUCTION</h2>
    <p>Sed ut perspiciatis unde omnis iste natus error sit voluptatem accusantium dolor emque laudantium, totam rem aperiam, eaque ipsa quae ab illo inventore veritatis et quasi architecto beatae vitae dicta sunt explicabo. Nemo enim ipsam voluptatem quia voluptas sit aspernatur aut odit aut fugit, sed quia consequuntur magni dolores eos qui ratione voluptatem sequi nesciunt.</p>
    <p>Neque porro quisquam est, qui dolorem ipsum quia dolor sit amet, consectetur, adipisci velit, sed quia non numquam eius modi tempora</p>
    <span class="btn">READ MORE <svg viewBox="0 0 20 20"><circle cx="10" cy="10" r="9" fill="#fff"/><path d="M5 10h8M10 6l4 4-4 4" stroke="#3a9a6a" stroke-width="2.4" fill="none"/></svg></span>
  </div>
</section>

<section class="service" style="top:1994px">
  <div class="service-text" style="left:130px;top:48px">
    <h2>PROFESSIONAL DEVELOPMENT</h2>
    <p>Sed ut perspiciatis unde omnis iste natus error sit voluptatem accusantium dolor emque laudantium, totam rem aperiam, eaque ipsa quae ab illo inventore veritatis et quasi architecto beatae vitae dicta sunt explicabo. Nemo enim ipsam voluptatem quia voluptas sit aspernatur aut odit aut fugit, sed quia consequuntur magni dolores eos qui ratione voluptatem sequi nesciunt.</p>
    <p>Neque porro quisquam est, qui dolorem ipsum quia dolor sit amet, consectetur, adipisci velit, sed quia non numquam eius modi tempora</p>
    <span class="btn">READ MORE <svg viewBox="0 0 20 20"><circle cx="10" cy="10" r="9" fill="#fff"/><path d="M5 10h8M10 6l4 4-4 4" stroke="#3a9a6a" stroke-width="2.4" fill="none"/></svg></span>
  </div>
  <div class="frame" style="left:661px;top:0"></div>
  <div class="photo photo-laptop" style="left:675px;top:15px" role="img" aria-label="Colleagues at a desk with a laptop and phones, seen from above"></div>
</section>

<footer class="footer">
  <div class="footer-body"></div>
  <svg class="footer-wave" viewBox="0 0 1200 100" preserveAspectRatio="none">
    <path d="M0 32 C250 100 500 75 700 50 C900 25 1080 20 1200 30 L1200 100 L0 100 Z" fill="#333"/>
    <path d="M0 28 C250 95 500 70 700 45 C750 38 790 33 815 30" stroke="#0c4a45" stroke-width="6" fill="none" stroke-linecap="round"/>
  </svg>
  <div class="footer-brand"><span>BRINDLE COVE</span><span class="brand-dot"></span></div>
  <nav class="footer-nav">Home<span>|</span>About Us<span>|</span>Coaching<span>|</span>Services<span>|</span>Testimonials<span>|</span>Contact</nav>
  <p class="copyright">© Brindle Cove 2019. All rights reserved</p>
  <div class="social" aria-label="Social links"><i></i><i></i><i></i><i></i></div>
</footer>
</body>
</html>
```